Little Amber Mornings Blog Re-Do Launch

I need a blog makeover. Someone started for me and they sold their company. The blog is primarily spiritual/inspirational. I would eventually like to monetize and launch some ebooks and/or other products. I am open to suggestions. I am learning as we go along, so please keep that in mind. The final design should be warm and welcoming. I am open to suggestions. I am looking to build a relationship.

Target Market(s)

women, moms, females with chronic health issues, moms of special needs kids, those who need encouragement

Industry/Entity Type

Religious

Number of Pages Required

4 page

Font styles to use
Sans Serif

Colors
eddcec
fdf9cf
ffffff

Requirements
Must have
• I would like my main page to have a short about section, relevant posts, recent posts, and archive posts. The main page should also have a place to subscribe as well a search feature.
Nice to have
• Buttons (grab my button), blogs I follow, e-cart capabilities

```html
<!DOCTYPE html>
<html lang="en">
<head>
<meta charset="utf-8">
<title>Little Amber Mornings</title>
<link href="https://fonts.googleapis.com/css2?family=Lato:wght@400;700;900&family=Libre+Baskerville:wght@400;700&display=swap" rel="stylesheet">
<style>
:root{
  --blush:#eddcec;
  --cream:#fdf9cf;
  --white:#ffffff;
  --ink:#1e2330;
  --text:#3a3f4a;
  --muted:#a3a8b0;
  --line:#e6e8ec;
  --link:#1f5fa8;
  --navy:#273554;
  --footer:#2c2c2c;
  --footer-text:#9b9b9b;
  --tag:#454545;
}
*{margin:0;padding:0;box-sizing:border-box}
html,body{width:1200px;height:2442px;overflow:hidden;background:var(--white);font-family:"Lato",sans-serif;color:var(--text)}
.page{position:relative;width:1200px;height:2442px}
.abs{position:absolute}

/* header */
.site-header{position:absolute;left:0;top:0;width:1200px;height:124px;background:var(--blush)}
.brand{position:absolute;left:98px;top:60px;font-family:"Libre Baskerville",serif;font-size:26px;color:var(--ink);white-space:nowrap}
.brand-mark{display:inline-block;width:16px;height:16px;background:var(--white);margin-right:12px;vertical-align:2px}
.search{position:absolute;left:545px;top:29px;width:233px;height:31px;background:var(--white);border-radius:6px;font-size:11px;color:var(--muted);padding:10px 12px;letter-spacing:.5px}
.search svg{position:absolute;right:10px;top:8px}
.pill{position:absolute;top:29px;height:31px;border-radius:6px;font-size:12px;font-family:"Libre Baskerville",serif;color:var(--ink);display:flex;align-items:center;justify-content:center;gap:7px;letter-spacing:.5px;white-space:nowrap}
.pill.register{left:806px;width:107px;background:var(--white)}
.pill.login{left:925px;width:105px;background:var(--cream)}
.cart{position:absolute;left:1064px;top:28px}
.main-nav{position:absolute;right:100px;top:86px;display:flex;gap:37px;font-size:14px;color:var(--ink);white-space:nowrap}

/* hero */
.hero{position:absolute;left:0;top:124px;width:1200px;height:589px;background:radial-gradient(ellipse at 62% 18%,#f4f7fb 0%,#c9d6e8 18%,#7f98c2 45%,#3e5a96 75%,#2a4380 100%)}
.hero-cross{position:absolute;left:640px;top:0;width:360px;height:589px;background:linear-gradient(90deg,rgba(225,228,232,.0),rgba(225,228,232,.35) 40%,rgba(225,228,232,0))}
.hero-title{position:absolute;left:132px;top:358px;font-family:"Libre Baskerville",serif;font-weight:700;font-size:24px;color:var(--white);white-space:nowrap}
.hero-text{position:absolute;left:132px;top:410px;font-family:"Libre Baskerville",serif;font-size:16.5px;line-height:25px;color:var(--white);white-space:nowrap}
.hero-btn{position:absolute;left:137px;top:511px;width:137px;height:35px;background:var(--cream);border-radius:6px;font-family:"Libre Baskerville",serif;font-size:11px;color:var(--ink);display:flex;align-items:center;justify-content:space-between;padding:0 13px;white-space:nowrap}
.slider-arrow{position:absolute;top:382px;width:38px;height:38px;border-radius:50%;background:rgba(255,255,255,.55);display:flex;align-items:center;justify-content:center}

/* panels */
.panel{position:absolute;background:var(--white);border:1px solid var(--line)}
.panel-title{font-size:14px;font-weight:900;letter-spacing:1.4px;color:var(--ink);text-transform:uppercase;white-space:nowrap}
.posts{left:98px;top:762px;width:660px;height:1008px;border-top:2px solid #f5f0cf}
.posts .accent{position:absolute;left:457px;top:-2px;width:93px;height:3px;background:var(--navy)}
.posts .head{position:absolute;left:0;top:0;width:100%;height:48px;border-bottom:1px solid var(--line)}
.posts .head .panel-title{position:absolute;left:26px;top:17px}
.posts .head .view{position:absolute;right:16px;top:18px;font-size:12px;color:var(--muted)}
.post{position:absolute;left:26px;width:607px;height:155px;border-bottom:1px solid var(--line)}
.post-media{position:absolute;left:0;top:0;width:189px;height:127px}
.post-tag{position:absolute;left:0;top:4px;background:var(--blush);font-size:12px;color:var(--ink);padding:4px 10px;white-space:nowrap}
.post-title{position:absolute;left:206px;top:0;font-size:14px;font-weight:700;color:var(--ink);white-space:nowrap}
.post-meta{position:absolute;left:206px;top:23px;font-size:11px;color:var(--muted);display:flex;gap:14px}
.post-excerpt{position:absolute;left:206px;top:47px;width:400px;font-size:11.5px;line-height:19px;color:var(--muted)}
.post-more{position:absolute;left:206px;top:115px;font-size:12px;font-weight:700;color:var(--link)}
.posts .foot{position:absolute;left:26px;top:970px;font-size:11px;font-weight:700;color:var(--ink)}

.side-box{left:783px;width:318px;border-top:3px solid #dfe4ea}
.side-box .panel-title{position:absolute;left:26px;top:22px}
.side-box .rule{position:absolute;left:0;top:44px;width:100%;height:1px;background:var(--line)}
.cat{position:absolute;left:26px;width:265px;font-size:11px;color:var(--ink);display:flex;justify-content:space-between;align-items:center}
.cat.lead{font-weight:700;color:var(--link);letter-spacing:1px}
.sub{position:absolute;left:26px;font-size:11px;color:var(--muted)}

.tabs{position:absolute;left:0;top:0;width:100%;height:44px;border-bottom:1px solid var(--line)}
.tab{position:absolute;top:0;height:44px;font-size:13px;font-weight:900;letter-spacing:1.2px;display:flex;align-items:center;justify-content:center;white-space:nowrap}
.tab.active{left:0;width:159px;color:var(--ink);background:var(--white);border-top:2px solid #f5f0cf}
.tab.off{left:159px;width:158px;color:var(--muted);background:#e9edef}
.recent{position:absolute;left:26px;width:265px;height:94px;border-bottom:1px solid var(--line)}
.recent-thumb{position:absolute;left:0;top:0;width:61px;height:60px}
.recent-title{position:absolute;left:77px;top:0;width:190px;font-size:13px;font-weight:700;line-height:21px;color:var(--ink)}
.recent-meta{position:absolute;left:77px;font-size:11px;color:var(--muted);white-space:nowrap}

.ad-banner{position:absolute;left:124px;top:1843px;width:624px;height:78px;background:linear-gradient(90deg,#e5e5e5 0%,#f1f1f1 26%,#5f9a1e 27%,#3f7a10 70%,#2f6a0a 100%)}

/* footer */
.site-footer{position:absolute;left:0;top:2077px;width:1200px;height:365px;background:var(--footer)}
.f-col{position:absolute;top:47px}
.f-head{font-size:13px;font-weight:700;color:var(--white);white-space:nowrap}
.social{position:absolute;top:87px;width:72px;height:93px;color:var(--white);font-size:12px;text-align:center}
.social .dot{width:14px;height:14px;border-radius:50%;background:var(--white);margin:22px auto 20px;opacity:.9}
.f-text{font-size:11.5px;line-height:19px;color:var(--footer-text)}
.f-link{font-size:11px;color:var(--footer-text);white-space:nowrap}
.f-link b{color:#4aa3e0}
.mail-input{position:absolute;top:130px;width:231px;height:28px;background:#f4f4f4;font-size:11px;color:var(--muted);padding:8px 16px}
.mail-btn{position:absolute;right:0;top:0;width:31px;height:28px;background:#d8cf6a;display:flex;align-items:center;justify-content:center}
.product{position:absolute;width:73px;height:73px}
.tags{position:absolute;left:868px;top:2165px;display:flex;flex-direction:column;gap:12px}
.tag-row{display:flex;gap:10px}
.tag{background:var(--tag);color:#b8b8b8;font-size:11px;padding:5px 10px;white-space:nowrap}
.tag.on{background:var(--blush);color:var(--ink)}
.copyright{position:absolute;left:0;top:2411px;width:1200px;text-align:center;font-size:10px;letter-spacing:.8px;color:#777}
</style>
</head>
<body>
<div class="page">

<header class="site-header">
  <div class="brand"><span class="brand-mark"></span>Little Amber Mornings</div>
  <div class="search">SEARCH
    <svg width="14" height="14" viewBox="0 0 14 14"><circle cx="6" cy="6" r="4.5" fill="none" stroke="#555" stroke-width="1.5"/><line x1="9.5" y1="9.5" x2="13" y2="13" stroke="#555" stroke-width="1.5"/></svg>
  </div>
  <div class="pill register">
    <svg width="9" height="11" viewBox="0 0 9 11"><rect x="0" y="4.5" width="9" height="6.5" fill="#333"/><path d="M2 4.5V3a2.5 2.5 0 0 1 5 0v1.5" fill="none" stroke="#333" stroke-width="1.4"/></svg>REGISTER</div>
  <div class="pill login">
    <svg width="9" height="11" viewBox="0 0 9 11"><rect x="0" y="4.5" width="9" height="6.5" fill="#333"/><path d="M2 4.5V3a2.5 2.5 0 0 1 5 0v1.5" fill="none" stroke="#333" stroke-width="1.4"/></svg>LOGIN</div>
  <svg class="cart" width="38" height="30" viewBox="0 0 38 30"><path d="M1 3h6l5 16h19l4-12H9" fill="none" stroke="#222" stroke-width="2.4" stroke-linejoin="round"/><path d="M12 9h21M13 14h18" stroke="#222" stroke-width="1.6"/><circle cx="14" cy="25" r="2.6" fill="#222"/><circle cx="29" cy="25" r="2.6" fill="#222"/></svg>
  <nav class="main-nav"><span>Home</span><span>About Us</span><span>Services</span><span>Gallery</span><span>Blog</span><span>news</span><span>Contact Us</span></nav>
</header>

<section class="hero" role="img" aria-label="Photo of a tall white cross against a bright cloudy blue sky">
  <div class="hero-cross"></div>
</section>
<h1 class="hero-title">LOREM IPSUM DOLOR</h1>
<p class="hero-text">LOREM IPSUM DOLOR SIT AMET, CONSECTETUR<br>ADIPISCING ELIT. DUIS TINCIDUNT EGET URNA<br>VEL MAXIMUS. NULLA SIT AMET</p>
<div class="hero-btn"><span>READ MORE</span>
  <svg width="14" height="14" viewBox="0 0 14 14"><circle cx="7" cy="7" r="6" fill="none" stroke="#333"/><path d="M4 7h6M7.5 4.5 10 7l-2.5 2.5" fill="none" stroke="#333"/></svg></div>
<div class="slider-arrow" style="left:24px"><svg width="12" height="16" viewBox="0 0 12 16"><path d="M9 2 3 8l6 6" fill="none" stroke="#2a4380" stroke-width="3"/></svg></div>
<div class="slider-arrow" style="left:1137px"><svg width="12" height="16" viewBox="0 0 12 16"><path d="M3 2l6 6-6 6" fill="none" stroke="#2a4380" stroke-width="3"/></svg></div>

<section class="panel posts">
  <div class="accent"></div>
  <div class="head"><h2 class="panel-title">Relevant Posts</h2><span class="view">View All</span></div>

  <article class="post" style="top:72px">
    <div class="post-media" role="img" aria-label="Photo of a kneeling figure in white robes drawing in sand" style="background:linear-gradient(135deg,#e8d9c2,#b58d63)"></div>
    <span class="post-tag">Praesent vol</span>
    <h3 class="post-title">Praesent tempus magna risus, ac lacinia velit lacinia</h3>
    <div class="post-meta"><span>&#9679; Jane Rowe</span><span>&#9638; 14th Dec 2015</span></div>
    <p class="post-excerpt">Lorem ipsum dolor sit amet, consectetur adipiscing elit. Aliquam aliquam non sapien nec rhoncus. Praesent quis tempor sapien. In ut pretium massa. Aliquam ac iaculis est.</p>
    <span class="post-more">Read more</span>
  </article>

  <article class="post" style="top:253px">
    <div class="post-media" role="img" aria-label="Photo of a glowing figure in golden heavenly light" style="background:radial-gradient(circle at 55% 40%,#fbf2b8,#b89a2c 55%,#4d4310)"></div>
    <span class="post-tag">Loerm ips</span>
    <h3 class="post-title">Morbi ac ultricies elit. Maecenas interdum cus eros</h3>
    <div class="post-meta"><span>&#9679; Jane Rowe</span><span>&#9638; 14th Dec 2015</span></div>
    <p class="post-excerpt">Lorem ipsum dolor sit amet, consectetur adipiscing elit. Aliquam aliquam non sapien nec rhoncus. Praesent quis tempor sapien. In ut pretium massa. Aliquam ac iaculis est.</p>
    <span class="post-more">Read more</span>
  </article>

  <article class="post" style="top:434px">
    <div class="post-media" role="img" aria-label="Photo of a crown of thorns on a dark background" style="background:linear-gradient(135deg,#1c1c1c,#5b534a 60%,#2a2622)"></div>
    <span class="post-tag">Contantry</span>
    <h3 class="post-title">Praesent tempus magna risus, ac lacinia velit lacinia</h3>
    <div class="post-meta"><span>&#9679; Jane Rowe</span><span>&#9638; 14th Dec 2015</span></div>
    <p class="post-excerpt">Lorem ipsum dolor sit amet, consectetur adipiscing elit. Aliquam aliquam non sapien nec rhoncus. Praesent quis tempor sapien. In ut pretium massa. Aliquam ac iaculis est.</p>
    <span class="post-more">Read more</span>
  </article>

  <article class="post" style="top:615px">
    <div class="post-media" role="img" aria-label="Photo of stacked stones on a warm sandy beach" style="background:linear-gradient(180deg,#f1dfa5,#d7ae63 60%,#9b7040)"></div>
    <span class="post-tag">Popilarsitamit lore</span>
    <h3 class="post-title">Praesent tempus magna risus, ac lacinia velit lacinia</h3>
    <div class="post-meta"><span>&#9679; Jane Rowe</span><span>&#9638; 14th Dec 2015</span></div>
    <p class="post-excerpt">Lorem ipsum dolor sit amet, consectetur adipiscing elit. Aliquam aliquam non sapien nec rhoncus. Praesent quis tempor sapien. In ut pretium massa. Aliquam ac iaculis est.</p>
    <span class="post-more">Read more</span>
  </article>

  <article class="post" style="top:796px">
    <div class="post-media" role="img" aria-label="Photo of a silhouetted crowd raising hands at a sunset concert" style="background:linear-gradient(180deg,#e9a64a,#a6501c 55%,#2a1408)"></div>
    <span class="post-tag">Popilar sit</span>
    <h3 class="post-title">Praesent tempus magna risus, ac lacinia velit lacinia</h3>
    <div class="post-meta"><span>&#9679; Jane Rowe</span><span>&#9638; 14th Dec 2015</span></div>
    <p class="post-excerpt">Lorem ipsum dolor sit amet, consectetur adipiscing elit. Aliquam aliquam non sapien nec rhoncus. Praesent quis tempor sapien. In ut pretium massa. Aliquam ac iaculis est.</p>
    <span class="post-more">Read more</span>
  </article>

  <div class="foot"><svg width="8" height="10" viewBox="0 0 8 10" style="margin-right:8px"><path d="M2 1l4 4-4 4" fill="none" stroke="#1e2330" stroke-width="2"/></svg>View All</div>
</section>

<div class="ad-banner" role="img" aria-label="Advertising banner for Brightpeak Hosting faster web hosting"></div>

<aside class="panel side-box" style="top:762px;height:331px">
  <h2 class="panel-title">Categories</h2><div class="rule"></div>
  <div class="cat lead" style="top:70px">LOREM ( 4 )</div>
  <div class="cat" style="top:105px"><span>FAITH ( 4 )</span><span style="font-size:16px;color:#888">+</span></div>
  <div class="cat" style="top:138px"><span>CONTANTRY ( 5 )</span><span style="font-size:16px;color:#888">&minus;</span></div>
  <div class="sub" style="top:177px">Praesent tempus magna</div>
  <div class="sub" style="top:202px">Ac lacinia</div>
  <div class="sub" style="top:228px">Velit lacinia</div>
  <div class="sub" style="top:253px">Egestas</div>
  <div class="cat" style="top:289px"><span>Tutorials</span><span style="font-size:16px;color:#888">+</span></div>
</aside>

<aside class="panel side-box" style="top:1114px;height:222px">
  <h2 class="panel-title">Blogs I Follow</h2><div class="rule"></div>
  <div class="sub" style="top:72px">Praesent tempus magna</div>
  <div class="sub" style="top:97px">Ac lacinia</div>
  <div class="sub" style="top:123px">Velit lacinia</div>
  <div class="sub" style="top:148px">Egestas</div>
</aside>

<aside class="panel" style="left:783px;top:1363px;width:318px;height:626px">
  <div class="tabs"><div class="tab active">RECENT POST</div><div class="tab off">ARCHIVE POSTS</div></div>
  <div class="recent" style="top:70px">
    <div class="recent-thumb" role="img" aria-label="Photo of a cross silhouette at sunset" style="background:linear-gradient(180deg,#c8c2b3,#3d3328)"></div>
    <div class="recent-title">Morbi ac ultricies elit. Maece-nas interdum dictum quam, at rhoncus eros</div>
    <div class="recent-meta" style="top:68px">Category &nbsp;|&nbsp; 14th Dec 2015</div>
  </div>
  <div class="recent" style="top:164px">
    <div class="recent-thumb" role="img" aria-label="Photo of a sunlit green forest path" style="background:radial-gradient(circle at 50% 40%,#eef7c4,#7cb23c 60%,#3f6e1c)"></div>
    <div class="recent-title">Morbi ac ultricies elit. Maece-nas interdum</div>
    <div class="recent-meta" style="top:48px">Category &nbsp;|&nbsp; 14th Dec 2015</div>
  </div>
  <div class="recent" style="top:258px">
    <div class="recent-thumb" role="img" aria-label="Photo of a cross on a grassy hill under blue sky" style="background:linear-gradient(180deg,#cfe0ef,#8fb3d4 55%,#5f8a3a)"></div>
    <div class="recent-title" style="font-weight:400">Maecenas interdum dictum quam, at rhoncus eros</div>
    <div class="recent-meta" style="top:48px">Category &nbsp;|&nbsp; 14th Dec 2015</div>
  </div>
  <div class="recent" style="top:352px">
    <div class="recent-thumb" role="img" aria-label="Photo of a white dove flying in blue sky" style="background:linear-gradient(180deg,#6f9fd6,#c6dcf2)"></div>
    <div class="recent-title">Morbi ac ultricies elit. Maece-nas interdum dictum</div>
    <div class="recent-meta" style="top:48px">Category &nbsp;|&nbsp; 14th Dec 2015</div>
  </div>
  <div class="recent" style="top:446px;height:120px">
    <div class="recent-thumb" role="img" aria-label="Photo of a cross against a stormy evening sky" style="background:linear-gradient(180deg,#8ea4c4,#2f3c55)"></div>
    <div class="recent-title" style="font-weight:400">Morbi ac ultricies elit. Maece-nas interdum dictum quam</div>
    <div class="recent-meta" style="top:48px">Category &nbsp;|&nbsp; 14th Dec 2015</div>
  </div>
  <div class="abs" style="left:26px;top:592px;font-size:11px;font-weight:700;color:#2a93c9;white-space:nowrap"><svg width="8" height="10" viewBox="0 0 8 10" style="margin-right:8px"><path d="M2 1l4 4-4 4" fill="none" stroke="#2a93c9" stroke-width="2"/></svg>View All Articles</div>
</aside>

<footer class="site-footer">
  <div class="f-col" style="left:98px"><h3 class="f-head">Let's Connect</h3></div>
  <div class="social" style="left:98px;background:#3b5a9a"><div class="dot"></div>2598</div>
  <div class="social" style="left:176px;background:#2aa7df"><div class="dot"></div>4576</div>
  <div class="social" style="left:257px;background:#dd4a38"><div class="dot"></div>1269</div>
  <p class="f-text abs" style="left:98px;top:190px;width:230px">Praesent volutpat non nulla vitae vehicula. Proin euismod id justo quis molestie. Proin ultrices, nisi eget consequat</p>
  <div class="f-link abs" style="left:98px;top:281px">Read more <b>&rsaquo;</b></div>

  <div class="f-col" style="left:355px"><h3 class="f-head">Mailing List</h3></div>
  <p class="f-text abs" style="left:355px;top:86px;width:240px">Sign up for our mailing list to get latest updates and offers.</p>
  <div class="mail-input" style="left:355px">Email address
    <div class="mail-btn"><svg width="12" height="10" viewBox="0 0 12 10"><path d="M1 5l3.5 3.5L11 1.5" fill="none" stroke="#333" stroke-width="2"/></svg></div></div>
  <div class="f-link abs" style="left:355px;top:168px;font-size:10px;color:#777">We respect your privacy</div>

  <div class="f-col" style="left:610px"><h3 class="f-head">Our Products</h3></div>
  <div class="product" role="img" aria-label="Illustrated scripture scene product" style="left:610px;top:88px;background:linear-gradient(135deg,#7aa6c8,#c9a96a)"></div>
  <div class="product" role="img" aria-label="Sacred heart artwork product" style="left:690px;top:88px;background:radial-gradient(circle,#e0583a,#5c1b12)"></div>
  <div class="product" role="img" aria-label="Blue world map artwork product" style="left:769px;top:88px;background:linear-gradient(135deg,#e8eef6,#6e96c8)"></div>
  <div class="product" role="img" aria-label="Line drawing artwork product" style="left:610px;top:168px;background:#f2f2f2"></div>
  <div class="product" role="img" aria-label="Cartoon illustration product" style="left:690px;top:168px;background:linear-gradient(135deg,#f6f6f6,#c7d9ee)"></div>
  <div class="product" role="img" aria-label="Word cloud artwork product" style="left:769px;top:168px;background:linear-gradient(135deg,#f5eaea,#b6463a)"></div>
  <div class="f-link abs" style="left:610px;top:258px">View more <b>&rsaquo;</b></div>

  <div class="f-col" style="left:868px"><h3 class="f-head">Popular Tags</h3></div>
</footer>
<div class="tags">
  <div class="tag-row"><span class="tag">Amazing</span><span class="tag">Popilar</span><span class="tag">Sitamit</span></div>
  <div class="tag-row"><span class="tag on">Lorem</span><span class="tag">Lorem sit</span><span class="tag">Dlo sit</span></div>
  <div class="tag-row"><span class="tag">Contantry pop</span><span class="tag">Contantry</span></div>
  <div class="tag-row"><span class="tag">Tidings</span><span class="tag">Lorem sit ami</span></div>
</div>
<div class="copyright">&copy; YOUR SITE 2015. ALL RIGHTS RESERVED</div>

</div>
</body>
</html>
```